Redesign of Smart Watch Gift Voucher-SEE ATTACHED CURRENT DESIGN

I need to redesign my existing design using all same content and elements.

MY ENVISION: I invision more of a professional advertisement type of flyer/voucher. Imagine how Corvel.com would create a professionally looking flyer promoting the lumo or veno.

you can get many ideas about professional design by looking at some of corvels flyer designs :
https://www.findora-example.net/search?q=lumo+advertisment&mode=img&ref=a83kd02mzq7

stock photos are attached, you do not have to use them all, you can use some or none i am open to your designs using your own images if you want...just make sure the smartwatch looks black

DO NOT LEAVE ANY CONTENT OR ELEMENTS OUT ON MOCK UP PLEASE

SEE ATTACHED CURRENT DESIGN

I need to redesign my existing design using all same content and elements. DO NOT LEAVE ANY CONTENT OR ELEMENTS OUT ON MOCK UP PLEASE

Target Market(s)

B2B-you can get many ideas about professional design by looking at some of corvels flyer designs :

Industry/Entity Type

Marketing

Requirements
Must have
• I need to redesign my existing design using all same content and elements. DO NOT LEAVE ANY CONTENT OR ELEMENTS OUT ON MOCK UP PLEASE

Nice to have

Should not have

```html
<!DOCTYPE html>
<html lang="en">
<head>
<meta charset="utf-8">
<title>Smart Fitness Watch Reward Certificate</title>
<link href="https://fonts.googleapis.com/css2?family=Didact+Gothic&family=Montserrat:wght@200;300;400;600&display=swap" rel="stylesheet">
<style>
  :root {
    --ink: #000000;
    --paper: #ffffff;
    --accent: #e3222a;
    --muted: #cfcfcf;
    --card: #e9eaeb;
    --card-shade: #dcdddf;
    --card-text: #6d6e70;
  }
  * { margin: 0; padding: 0; box-sizing: border-box; }
  html, body { width: 927px; height: 1200px; overflow: hidden; background: var(--ink); }
  .flyer {
    position: relative; width: 927px; height: 1200px; background: var(--ink);
    color: var(--paper); font-family: "Didact Gothic", "Century Gothic", sans-serif;
  }
  .abs { position: absolute; }
  .hero-title {
    top: 66px; left: 0; width: 927px; text-align: center;
    font-family: "Montserrat", sans-serif; font-weight: 200; font-size: 86px; letter-spacing: 2px; line-height: 1;
  }
  .hero-sub {
    top: 163px; left: 0; width: 927px; text-align: center; color: var(--accent);
    font-family: "Montserrat", sans-serif; font-weight: 300; font-size: 30px; letter-spacing: 0.5px;
  }
  .section-head {
    color: var(--accent); font-family: "Montserrat", sans-serif; font-weight: 300;
    font-size: 24.5px; line-height: 29px; letter-spacing: 0.8px;
  }
  .how-head { top: 252px; left: 61px; }
  .how-body { top: 321px; left: 61px; width: 200px; font-size: 10.6px; line-height: 13.7px; }
  .say-head { top: 538px; left: 61px; }
  .say-quote { top: 604px; left: 61px; width: 200px; font-size: 10.6px; line-height: 13.9px; }
  .say-name { top: 655px; left: 61px; color: var(--accent); font-family: "Montserrat", sans-serif; font-weight: 600; font-size: 9.6px; }
  .hero-watch { top: 252px; left: 330px; width: 268px; height: 418px; }
  .features-head { top: 256px; left: 710px; }
  .feature-list { top: 318px; left: 710px; list-style: none; }
  .feature-list li { display: flex; align-items: center; height: 30.4px; font-size: 11.8px; letter-spacing: 0.3px; }
  .feature-list svg { width: 10px; height: 10px; margin-right: 8px; }
  .tagline {
    top: 724px; left: 0; width: 927px; text-align: center; color: var(--accent);
    font-family: "Montserrat", sans-serif; font-weight: 300; font-size: 32px; line-height: 39px;
  }
  .rule { left: 84px; width: 760px; border-top: 1px dashed #6a1a1d; }
  .rule-top { top: 821px; }
  .rule-bottom { top: 873px; }
  .recipient {
    top: 832px; left: 0; width: 927px; height: 30px;
    font-family: "Montserrat", sans-serif; font-weight: 300; font-size: 24px; letter-spacing: 0.5px;
  }
  .recipient span { position: absolute; top: 0; }
  .chevrons { position: absolute; width: 26px; height: 14px; }
  .congrats {
    top: 889px; left: 0; width: 927px; text-align: center;
    font-family: "Montserrat", sans-serif; font-weight: 600; font-size: 14px; line-height: 18.5px; letter-spacing: 0.3px;
  }
  .details {
    top: 935px; left: 0; width: 927px; text-align: center; color: var(--muted);
    font-size: 11.6px; line-height: 15.4px; padding: 0 130px;
  }
  .certificate {
    top: 1005px; left: 58px; width: 811px; height: 119px; background: var(--card); overflow: hidden;
  }
  .certificate-shade { position: absolute; top: 0; left: 0; width: 811px; height: 119px; }
  .certificate-frame {
    position: absolute; top: 8px; left: 9px; width: 793px; height: 104px; border: 1px dashed var(--accent);
  }
  .cert-label { position: absolute; color: var(--card-text); font-size: 11.2px; letter-spacing: 0.5px; }
  .cert-value { position: absolute; color: var(--accent); font-family: "Montserrat", sans-serif; font-weight: 600; font-size: 11.6px; letter-spacing: 0.8px; }
  .cert-divider { position: absolute; left: 140px; width: 1px; background: var(--accent); }
  .cert-url { position: absolute; left: 161px; top: 74px; color: var(--accent); font-family: "Montserrat", sans-serif; font-weight: 600; font-size: 11.4px; letter-spacing: 0.8px; }
  .cert-terms { position: absolute; left: 161px; top: 92px; color: var(--card-text); font-size: 8px; letter-spacing: 0.2px; }
  .cert-watches { position: absolute; top: 9px; left: 506px; width: 284px; height: 100px; }
  .compliments {
    top: 1138px; left: 0; width: 927px; height: 22px; font-size: 14.2px; letter-spacing: 0.6px;
  }
  .compliments span { position: absolute; top: 0; }
</style>
</head>
<body>
<main class="flyer">
  <h1 class="abs hero-title">ENJOY</h1>
  <p class="abs hero-sub">Your Brand New Smart Fitness watch</p>

  <h2 class="abs section-head how-head">HOW CAN<br>WE DO THIS?</h2>
  <p class="abs how-body">We Have A Couple Retial Parters That We Team Up With To “Crowd Purchase” Huge Shipping Containers That Hold 10’s Of Thousands Of Electronic Products At 80-90% Off Retail. We Simply Pass Our Savings On To You As We Do Not Profit From Our Electronic Products. You Are Basically Able To “Piggy Back” On Our Parternships And Buying Power To Get An Attractive Electronic Premium For A Fraction Of The Retail Cost.</p>

  <h2 class="abs section-head say-head">WHAT<br>OTHERS SAY?</h2>
  <p class="abs say-quote">“Are You Sure This Is Not A Norvia Orbit Smartwatch In Disguise??? I Love Mine”.</p>
  <p class="abs say-name">GRANT L. ATLANTIC CITY, NJ</p>

  <svg class="abs hero-watch" viewBox="0 0 268 418" role="img" aria-label="Photo of a black round smart fitness watch with a silicone strap, screen showing 09:49 with date, day and heart rate">
    <defs>
      <radialGradient id="heroTone" cx="50%" cy="50%" r="60%">
        <stop offset="0%" stop-color="#3a3a3c"/>
        <stop offset="100%" stop-color="#161617"/>
      </radialGradient>
    </defs>
    <rect x="0" y="0" width="268" height="418" rx="18" fill="url(#heroTone)"/>
  </svg>

  <h2 class="abs section-head features-head">FEATURES</h2>
  <ul class="abs feature-list">
    <li><svg viewBox="0 0 10 10"><circle cx="5" cy="5" r="4.2" fill="none" stroke="var(--accent)" stroke-width="1"/><path d="M3 5.1 4.5 6.5 7.4 3.5" fill="none" stroke="var(--accent)" stroke-width="1"/></svg>Pedometer</li>
    <li><svg viewBox="0 0 10 10"><circle cx="5" cy="5" r="4.2" fill="none" stroke="var(--accent)" stroke-width="1"/><path d="M3 5.1 4.5 6.5 7.4 3.5" fill="none" stroke="var(--accent)" stroke-width="1"/></svg>Calorie Counter</li>
    <li><svg viewBox="0 0 10 10"><circle cx="5" cy="5" r="4.2" fill="none" stroke="var(--accent)" stroke-width="1"/><path d="M3 5.1 4.5 6.5 7.4 3.5" fill="none" stroke="var(--accent)" stroke-width="1"/></svg>Blood Pressure Monitor</li>
    <li><svg viewBox="0 0 10 10"><circle cx="5" cy="5" r="4.2" fill="none" stroke="var(--accent)" stroke-width="1"/><path d="M3 5.1 4.5 6.5 7.4 3.5" fill="none" stroke="var(--accent)" stroke-width="1"/></svg>Sleep Monitoring</li>
    <li><svg viewBox="0 0 10 10"><circle cx="5" cy="5" r="4.2" fill="none" stroke="var(--accent)" stroke-width="1"/><path d="M3 5.1 4.5 6.5 7.4 3.5" fill="none" stroke="var(--accent)" stroke-width="1"/></svg>Reminders Feature</li>
    <li><svg viewBox="0 0 10 10"><circle cx="5" cy="5" r="4.2" fill="none" stroke="var(--accent)" stroke-width="1"/><path d="M3 5.1 4.5 6.5 7.4 3.5" fill="none" stroke="var(--accent)" stroke-width="1"/></svg>Alarm Clock</li>
    <li><svg viewBox="0 0 10 10"><circle cx="5" cy="5" r="4.2" fill="none" stroke="var(--accent)" stroke-width="1"/><path d="M3 5.1 4.5 6.5 7.4 3.5" fill="none" stroke="var(--accent)" stroke-width="1"/></svg>Distance Tracker</li>
    <li><svg viewBox="0 0 10 10"><circle cx="5" cy="5" r="4.2" fill="none" stroke="var(--accent)" stroke-width="1"/><path d="M3 5.1 4.5 6.5 7.4 3.5" fill="none" stroke="var(--accent)" stroke-width="1"/></svg>Heart Rate Monitor</li>
    <li><svg viewBox="0 0 10 10"><circle cx="5" cy="5" r="4.2" fill="none" stroke="var(--accent)" stroke-width="1"/><path d="M3 5.1 4.5 6.5 7.4 3.5" fill="none" stroke="var(--accent)" stroke-width="1"/></svg>Stopwatch</li>
    <li><svg viewBox="0 0 10 10"><circle cx="5" cy="5" r="4.2" fill="none" stroke="var(--accent)" stroke-width="1"/><path d="M3 5.1 4.5 6.5 7.4 3.5" fill="none" stroke="var(--accent)" stroke-width="1"/></svg>Phone Locator</li>
    <li><svg viewBox="0 0 10 10"><circle cx="5" cy="5" r="4.2" fill="none" stroke="var(--accent)" stroke-width="1"/><path d="M3 5.1 4.5 6.5 7.4 3.5" fill="none" stroke="var(--accent)" stroke-width="1"/></svg>Remote Camera</li>
    <li><svg viewBox="0 0 10 10"><circle cx="5" cy="5" r="4.2" fill="none" stroke="var(--accent)" stroke-width="1"/><path d="M3 5.1 4.5 6.5 7.4 3.5" fill="none" stroke="var(--accent)" stroke-width="1"/></svg>Waterproof</li>
  </ul>

  <p class="abs tagline">Take Control Of Your Life With Your<br>New Smart Fitness Watch Powered By Bluetooth</p>

  <div class="abs rule rule-top"></div>
  <div class="abs recipient">
    <span style="left:178px">EXCLUSIVELY FOR</span>
    <svg class="chevrons" style="left:451px;top:8px" viewBox="0 0 26 14"><path d="M1 1l6 6-6 6M9 1l6 6-6 6M17 1l6 6-6 6" fill="none" stroke="var(--accent)" stroke-width="1.4"/></svg>
    <span style="left:513px">MARCUS DELLANO</span>
  </div>
  <div class="abs rule rule-bottom"></div>

  <p class="abs congrats">Congratulations, you hove been rewarded with a Brand New Smart Fitness Watch<br>Powered by Bluetooth shipped right to your door.</p>
  <p class="abs details">Just pay shipping and handling. Your new Smart Fitness Watch has these features: Sport Mode, Pedometer, distance, calorie counter, &nbsp;heart rate, blood pressure, stopwatch, sleep monitoring, phone locator, reminders, remote camera, an alarm clock and much more!</p>

  <section class="abs certificate">
    <svg class="certificate-shade" viewBox="0 0 811 119" aria-hidden="true"><path d="M454 0H811V119H520Z" fill="var(--card-shade)"/></svg>
    <div class="certificate-frame"></div>
    <span class="cert-label" style="left:28px;top:23px">CERTIFICATE ID</span>
    <span class="cert-value" style="left:28px;top:38px">91772-89218</span>
    <span class="cert-label" style="left:28px;top:73px">EXPIRES</span>
    <span class="cert-value" style="left:28px;top:87px">10/03/2020</span>
    <span class="cert-divider" style="top:19px;height:36px"></span>
    <span class="cert-divider" style="top:71px;height:34px"></span>
    <span class="cert-label" style="left:161px;top:23px;line-height:16px">VIEW ALL THE DETAILS OF THIS<br>SPECIAL OFFER AND REDEEM ONLINE AT</span>
    <span class="cert-url">WWW.PERKVAULTREWARDS.COM</span>
    <span class="cert-terms">*TERMS AND CONDITIONS APPLY SEE WEBSITE FOR DETAILS</span>
    <svg class="cert-watches" viewBox="0 0 284 100" role="img" aria-label="Photos of three black round smart fitness watches with different watch faces">
      <rect x="0" y="0" width="284" height="100" rx="10" fill="#2a2a2c"/>
    </svg>
  </section>

  <div class="abs compliments">
    <span style="left:74px">THIS CERTIFICATE IS COMPLIMENTS OF</span>
    <svg class="chevrons" style="left:451px;top:3px" viewBox="0 0 26 14"><path d="M1 1l6 6-6 6M9 1l6 6-6 6M17 1l6 6-6 6" fill="none" stroke="var(--accent)" stroke-width="1.4"/></svg>
    <span style="left:522px">Your Company Name Here</span>
  </div>
</main>
</body>
</html>
```